Homepage Redesign for Healthcare Tech Company

This is for a redesign of our current homepage. We have specific notes and a Mockup and we need a great designer to bring it to life and make it look sophisticated and professional. Please see the Current Page (attached and online) as well as the Notes doc and Mockup PPT, both attached, for what we need.

Overall, look at the current page as a sketch of what it could be. We would like a design that really nails the structure of both the overall page and the pipeline (that runs through Sections 1-4), so that it looks like one, clean, custom design (not pieced together). It’s important that the basic structure of the pipeline, especially the transition from icons to screenshots (starting in section 2, and mostly in section 3) all flow together well and look like a deliberate, well thought-out design. Please include that, and at least the headlines for each section, in any initial submissions.

We will be building out of website beyond just this page, and would be great to work with a designer we can continue working with on the website, the graphical screenshots and some infographics. Not a must but definitely an option if you would like. We didn’t include all pages in this project, because we would like the designer to focus all energy on creating a well thought-out homepage design with the wow factor, and we can build it out together from there. For now, we would like just 2 additional general theme pages (one smaller page for a couple paragraphs of text only and one with a few uniform sections, with room for text and small graphic-see notes).

Our customers are healthcare companies – both Doctors and IT professionals of medium to large healthcare organizations who support doctors. We are experts in healthcare interoperability technology and the page should reflect that. Medical Record documentation is an expensive time-consuming massive headache for our customer base. What we are offering is a truly groundbreaking solution that leverages the best technology available to bring them something that wasn’t possible before – ALL of their patient data in one enriched and linked document, delivered to their current workflow. It's an expensive solution but very impactful in terms of better patient care and dramatically streamlined workflow - the homepage needs to reflect that. Please take the time to understand the solution we offer and just let me know if you need clarification – I’m happy to answer any questions.

Thanks!

SEE ATTACHMENTS, and also this more detailed breakdown of the sections: https://qv.fx/Tr4mPz

Target Market(s)

Doctors, IT Professionals in the Healthcare field, Medical Coders..but focus should be on Doctors

Number of Pages Required

1 page

Colors
0355a3
3276b5
0293ce
6b449b
886aae
b7a5cd
00a990
33b8a4
86cfc6

Requirements
Must have
• - Sophisticated, professional, masterful layout
- Must refer to the attached DESIGN NOTES.doc (about 2 pages) and MOCKUP.PPT but bring the idea to life in an innovative way. In general, we collect all medical records, summarize and unify into 1 document that we send straight into each patient file, but referring to the actual notes to truly get what we do and what we need it is a must.
- Framing/background emphasis for provided screenshots (even if these screenshots don't fit exactly, we will make them fit after)
- Emphasis on the fact that clicking the View Source buttons in the Lumora (what we call our product) opens the actual source documents (underlying medical record) - this is a big deal for doctors and medical coders.
- Final design should be in editable PSD file
Nice to have
• Animation. We are asking for design only because we want the best design possible but we would definitely choose a great animated design (assuming that means you'd need to code it too - let me know) and ensure that you are paid the extra for coding if you need to code it yourself.
Should not have
• template feel - should look custom
cheesy photos of models dressed as doctors

```html
<!DOCTYPE html>
<html lang="en">
<head>
<meta charset="utf-8">
<title>Clinivue — Unified Patient Intelligence</title>
<link href="https://fonts.googleapis.com/css2?family=Outfit:wght@300;400;500;600&display=swap" rel="stylesheet">
<style>
:root{
  --teal:#00a990;--teal-2:#33b8a4;--teal-3:#86cfc6;
  --purple:#6b449b;--purple-2:#886aae;--lilac:#b7a5cd;
  --blue:#0293ce;
  --ink:#07080c;--navy:#121725;--navy-2:#1b2133;--footer:#141826;
  --text:#ffffff;--muted:#a9adb8;--dim:#7c8190;
}
*{box-sizing:border-box;margin:0;padding:0}
html,body{width:1200px;height:4181px;overflow:hidden;background:var(--ink)}
body{font-family:"Outfit",Arial,sans-serif;color:var(--text)}
section,header,footer{position:relative;width:1200px;overflow:hidden}
.abs{position:absolute}
.btn{display:inline-block;font-size:11px;font-weight:500;letter-spacing:.5px;text-transform:uppercase;color:#fff;padding:0;text-align:center}
.btn-teal{background:var(--teal)}
.btn-purple{background:var(--purple)}

/* hero */
.hero{height:641px;background:#12151d}
.hero-photo{position:absolute;inset:0;background:radial-gradient(ellipse at 62% 55%,#3b4250 0%,#1d222c 40%,#0f1117 80%)}
.nav a{position:absolute;top:40px;font-size:14px;color:#fff;text-decoration:none}
.brand{position:absolute;left:455px;top:30px;display:flex;align-items:center;gap:12px;font-size:31px;font-weight:400;letter-spacing:1px}
.brand i{width:30px;height:30px;background:var(--teal);display:block}
.hero h1{position:absolute;left:88px;top:248px;font-size:40px;font-weight:400;letter-spacing:.5px}
.hero .lead{position:absolute;left:88px;top:305px;width:600px;font-size:17px;font-weight:500;line-height:21px}
.hero .copy{position:absolute;left:88px;top:364px;width:650px;font-size:13px;line-height:19px;color:#e4e6ea}

/* sources */
.sources{height:704px;background:var(--ink)}
.sec-title{position:absolute;left:0;width:1200px;text-align:center;font-size:36px;font-weight:400}
.sec-sub{position:absolute;left:0;width:1200px;text-align:center;font-size:16px;color:var(--muted);line-height:20px}
.src h3{font-size:22px;font-weight:400;margin-bottom:12px}
.src p{font-size:11px;line-height:17px;color:var(--muted)}
.src.right-al{text-align:right}
.network{position:absolute;left:0;top:0}

/* c-cda */
.ccda{height:482px;background:linear-gradient(135deg,#0f3d41 0%,#12343f 45%,#151d2e 100%)}
.ccda h2{position:absolute;left:88px;top:129px;font-size:37px;font-weight:400;line-height:46px}
.ccda .copy{position:absolute;left:88px;top:228px;width:660px;font-size:13px;line-height:19px;color:var(--muted)}
.ccda .copy p+p{margin-top:17px}
.doc{position:absolute;left:820px;top:39px;width:289px;height:398px;background:#2a2c33;border-radius:10px 0 10px 10px;box-shadow:0 10px 30px rgba(0,0,0,.5);clip-path:polygon(0 0,78% 0,100% 16%,100% 100%,0 100%)}
.doc-fold{position:absolute;left:1045px;top:39px;width:64px;height:64px;background:#3a3d45;clip-path:polygon(0 0,100% 100%,0 100%)}
.doc ul{position:absolute;left:18px;top:96px;width:255px;list-style:none}
.doc li{font-family:Arial,sans-serif;font-size:14px;color:#fff;height:20px;line-height:18px;padding-left:6px;border:1px solid #5a5d66;background:#34363d;margin-bottom:4.6px}

/* insights */
.insights{height:538px;background:var(--navy)}
.shot{position:absolute;top:62px;width:320px;height:201px;background:#fff;border-radius:3px;box-shadow:0 0 0 2px #283048}
.insights h3{position:absolute;top:296px;width:320px;font-size:22px;font-weight:400;line-height:29px}
.insights p{position:absolute;width:310px;font-size:12.5px;line-height:19px;color:var(--muted)}

/* delivered */
.delivered{height:745px;background:linear-gradient(180deg,#0f3d41 0%,#0d1a24 45%,#0a0c13 100%)}
.ehr-row{position:absolute;left:41px;top:186px;width:1118px;display:flex;gap:10px}
.ehr{flex:1;height:88px;background:#15181f;border:1px solid #262a33;display:flex;align-items:center;justify-content:center;font-size:18px;color:#c6c9d0;font-weight:500}
.tablet-frame{position:absolute;left:335px;top:299px;width:527px;height:378px;border:2px solid var(--teal);border-radius:16px;background:#0d0f17;box-shadow:0 0 0 2px var(--purple) inset}
.tablet{position:absolute;left:14px;top:14px;width:495px;height:346px;background:#f2f3f5;border-radius:18px}
.screen{position:absolute;left:45px;top:20px;width:405px;height:306px;background:#fff;overflow:hidden}

/* features */
.features{height:300px;background:var(--navy-2)}
.feat{position:absolute;top:40px;width:260px;margin-left:-130px;text-align:center}
.feat svg{display:block;margin:0 auto 20px}
.feat h3{font-size:22px;font-weight:400;margin-bottom:12px}
.feat p{font-size:12px;line-height:17px;color:var(--muted);width:210px;margin:0 auto}

/* blog */
.blog{height:517px;background:var(--navy-2)}
.post{position:absolute;top:127px;width:320px;height:330px}
.post-img{position:absolute;left:0;top:0;width:320px;height:199px;background:linear-gradient(135deg,#e9ecf2 0%,#b8c3d6 45%,#5d6d8c 100%)}
.post-img.dark{background:linear-gradient(135deg,#2f3c55 0%,#1d2536 50%,#0d1220 100%)}
.post-cap{position:absolute;left:44px;top:162px;width:256px;height:109px;background:#0c0e15;padding:28px 30px 0 27px;font-size:16px;line-height:24px}
.post .btn{position:absolute;left:71px;top:292px;width:112px;height:32px;line-height:32px}

/* footer */
.site-footer{height:254px;background:var(--footer)}
.site-footer p{position:absolute;left:88px;width:1020px;font-size:13px;line-height:19px;color:var(--muted)}
.site-footer .legal{font-size:11px}
.foot-mark{position:absolute;left:1073px;top:203px;width:36px;height:36px;border:2px solid #fff}
</style>
</head>
<body>

<header class="hero">
  <div class="hero-photo" role="img" aria-label="Dark photo of an open hand beneath a glowing network of medical data icons"></div>
  <nav class="nav">
    <a href="#" style="left:88px">About Us</a>
    <a href="#" style="left:179px">Features</a>
    <a href="#" style="left:270px">Process</a>
    <a href="#" style="left:838px">Team</a>
    <a href="#" style="left:905px">Clients</a>
  </nav>
  <div class="brand"><i></i>CLINIVUE</div>
  <a class="btn btn-teal abs" style="left:984px;top:32px;width:128px;height:30px;line-height:30px">Request Access</a>
  <h1>Unified Patient Intelligence</h1>
  <p class="lead">Each patients’ full medical history, summary and analysis in one comprehensive health record</p>
  <p class="copy">Clinivue collects patients’ records from all sources of external clinical data, synthesizes the captured data into one composite health record, abstracts all HCC, MIPS and HEDIS opportunities, and delivers them directly into your EHR, all in a matter of hours.</p>
  <a class="btn btn-purple abs" style="left:88px;top:451px;width:128px;height:30px;line-height:30px">Request Access</a>
</header>

<section class="sources">
  <h2 class="sec-title" style="top:56px">Your Patients’ Full Medical History From All Sources</h2>
  <p class="sec-sub" style="top:112px">Each patients’ full medical history, summary and analysis in one<br>comprehensive health record</p>

  <svg class="network" width="1200" height="704" viewBox="0 0 1200 704">
    <defs>
      <linearGradient id="orb" x1="0" y1="0" x2="1" y2="1">
        <stop offset="0" stop-color="#00a990"/><stop offset="1" stop-color="#6b449b"/>
      </linearGradient>
    </defs>
    <g fill="none" stroke-width="1.5">
      <path d="M447 273 V310 H540" stroke="#00a990"/>
      <path d="M754 273 V310 H662" stroke="#00a990"/>
      <path d="M420 418 H490 V370 H508" stroke="#6b449b"/>
      <path d="M777 418 H720 V370 H694" stroke="#6b449b"/>
      <path d="M451 500 V395 H520" stroke="#00a990"/>
      <path d="M745 505 V395 H680" stroke="#00a990"/>
    </g>
    <circle cx="601" cy="353" r="93" fill="none" stroke="#00a990" stroke-width="1.5" stroke-dasharray="5 5"/>
    <circle cx="601" cy="353" r="82" fill="#1a1d27"/>
    <text x="601" y="331" fill="#fff" font-family="Outfit,Arial,sans-serif" font-size="22" text-anchor="middle">Clinivue</text>
    <text x="601" y="359" fill="#fff" font-family="Outfit,Arial,sans-serif" font-size="22" text-anchor="middle">Clinical Data</text>
    <text x="601" y="387" fill="#fff" font-family="Outfit,Arial,sans-serif" font-size="22" text-anchor="middle">Network</text>

    <g stroke="#fff" stroke-width="2.5" fill="none" stroke-linecap="round" stroke-linejoin="round">
      <circle cx="447" cy="233" r="40" fill="url(#orb)" stroke="none"/>
      <rect x="428" y="218" width="38" height="26" rx="2"/><path d="M440 252 H454 M447 244 V252"/>
      <circle cx="754" cy="233" r="40" fill="url(#orb)" stroke="none"/>
      <rect x="738" y="224" width="32" height="26" rx="2"/><rect x="744" y="214" width="14" height="10"/><path d="M762 232 h4 M762 238 h4 M762 244 h4"/>
      <circle cx="380" cy="418" r="40" fill="url(#orb)" stroke="none"/>
      <path d="M366 400 V414 a10 10 0 0 0 20 0 V400 M376 424 V432 a8 8 0 0 0 16 0 V424"/><circle cx="392" cy="420" r="4"/>
      <circle cx="817" cy="418" r="40" fill="url(#orb)" stroke="none"/>
      <path d="M800 408 H834 L826 400 M834 428 H800 L808 436"/>
      <circle cx="451" cy="540" r="40" fill="url(#orb)" stroke="none"/>
      <path d="M458 522 L470 534 M464 528 L442 550 a6 6 0 0 1 -9 -9 L455 519 M440 540 H452"/>
      <circle cx="745" cy="545" r="40" fill="url(#orb)" stroke="none"/>
      <path d="M745 524 L762 530 V544 C762 556 752 563 745 566 C738 563 728 556 728 544 V530 Z"/>
    </g>
  </svg>

  <div class="src right-al abs" style="left:137px;top:196px;width:240px">
    <h3>EMR Networks</h3>
    <p>Connected to 800,000 Physician EMR databases and over 60,000 hospitals across the country.</p>
  </div>
  <div class="src abs" style="left:823px;top:196px;width:320px">
    <h3>Provider Faxes</h3>
    <p>Fax records received from PCPs and specialists are converted into structured, searchable electronic records (C-CD) for ingestion into the Clinivue Lumora™.</p>
  </div>
  <div class="src right-al abs" style="left:40px;top:338px;width:280px">
    <h3 style="line-height:29px">RX Data or US<br>Pharmacies</h3>
    <p>Comprehensive medication history including medication starts, adherence, and switching behavior is collected from national and regional pharmacy data feeds. This includes specialized pharmacies.</p>
  </div>
  <div class="src abs" style="left:880px;top:362px;width:260px">
    <h3>HIE Networks</h3>
    <p>Aggregating from 32 Health Information Exchange networks for real-time access to clinical data.</p>
  </div>
  <div class="src right-al abs" style="left:67px;top:520px;width:310px">
    <h3>Diagnostic Labs</h3>
    <p>Clinivue is directly connected to all major diagnostic testing laboratories, enabling collection of all lab results.</p>
  </div>
  <div class="src abs" style="left:823px;top:520px;width:335px">
    <h3>Claims Databases</h3>
    <p>Connected to the nation’s largest clearinghouses for open and closed claims submission and processing, including Medicare Part A, B and D data for 53 million Medicare beneficiaries. This includes Medical &amp; Rx Open/Closed Claims EDI and Remittance ERI.</p>
  </div>
</section>

<section class="ccda">
  <h2>Transformed Into 1<br>Composite C-Cda Heath Record</h2>
  <div class="copy">
    <p>The Clinivue synthesis engine utilizes OCR, advanced parsing techniques, Clinical Natural Language Processing (cNLP), proprietary logic and NPI matching to clean, de-duplicate, structure and enrich all inputs from data acquisition.</p>
    <p>The normalized data is unified into the Lumora C-CDA, an enhanced composite longitudinal record in C-CDA format, the industry standard for all interoperability initiatives</p>
  </div>
  <div class="doc">
    <svg class="abs" style="left:122px;top:18px" width="56" height="62" viewBox="0 0 56 62" fill="none" stroke="#fff" stroke-width="2">
      <path d="M8 2 H38 L48 12 V40 M8 2 V28"/><path d="M14 12 H32 M14 18 H40 M14 24 H40"/>
      <rect x="2" y="28" width="52" height="24" rx="2"/>
      <text x="28" y="45" fill="#fff" stroke="none" font-family="Arial,sans-serif" font-size="13" text-anchor="middle">C-CDA</text>
      <path d="M8 52 V60 H48 V52"/>
    </svg>
    <ul>
      <li>Insurance Providers</li><li>Problems</li><li>Results</li>
      <li>Allergies, Adverse Reactions, Alerts</li><li>Immunizations</li><li>Medications</li>
      <li>Vital Signs</li><li>Procedures</li><li>Family History</li>
      <li>Social History</li><li>Encounters</li><li>Plan of Care</li>
    </ul>
  </div>
  <div class="doc-fold"></div>
</section>

<section class="insights">
  <svg class="shot" style="left:88px" viewBox="0 0 320 201">
    <rect x="0" y="0" width="320" height="201" fill="#fff"/>
    <rect x="6" y="6" width="8" height="8" fill="#0355a3"/>
    <g fill="#c8ccd4">
      <rect x="18" y="8" width="50" height="4"/><rect x="160" y="8" width="26" height="4"/><rect x="280" y="8" width="28" height="4"/>
      <rect x="6" y="42" width="74" height="5" fill="#555"/>
      <rect x="6" y="58" width="300" height="3"/><rect x="6" y="66" width="300" height="1"/>
      <rect x="6" y="92" width="48" height="5" fill="#555"/>
      <rect x="6" y="106" width="300" height="3"/><rect x="6" y="114" width="300" height="1"/>
      <rect x="6" y="136" width="40" height="5" fill="#555"/>
      <rect x="6" y="150" width="160" height="3"/><rect x="6" y="158" width="300" height="1"/>
      <rect x="6" y="178" width="40" height="5" fill="#555"/>
      <rect x="6" y="192" width="300" height="3"/>
    </g>
  </svg>
  <svg class="shot" style="left:440px" viewBox="0 0 320 201">
    <rect width="320" height="201" fill="#fff"/>
    <rect x="22" y="8" width="8" height="8" fill="#0355a3"/>
    <rect x="34" y="10" width="50" height="4" fill="#555"/><rect x="124" y="8" width="70" height="4" fill="#555"/><rect x="250" y="8" width="48" height="4" fill="#555"/>
    <rect x="22" y="34" width="276" height="7" fill="#e4e6ea"/>
    <g fill="#c8ccd4">
      <rect x="22" y="46" width="200" height="3"/><rect x="22" y="58" width="180" height="3"/><rect x="22" y="70" width="200" height="3"/>
      <rect x="22" y="82" width="170" height="3"/><rect x="22" y="94" width="190" height="3"/><rect x="22" y="106" width="160" height="3"/>
      <rect x="22" y="118" width="200" height="3"/><rect x="22" y="130" width="150" height="3"/><rect x="22" y="142" width="190" height="3"/>
      <rect x="22" y="154" width="120" height="3"/><rect x="22" y="166" width="90" height="3"/><rect x="22" y="178" width="180" height="3"/>
    </g>
    <g fill="#33b8a4"><rect x="255" y="46" width="14" height="3"/><rect x="255" y="70" width="14" height="3"/><rect x="255" y="94" width="14" height="3"/><rect x="255" y="118" width="14" height="3"/><rect x="255" y="142" width="14" height="3"/><rect x="255" y="166" width="14" height="3"/></g>
  </svg>
  <svg class="shot" style="left:791px" viewBox="0 0 320 201">
    <rect width="320" height="201" fill="#fff"/>
    <rect x="0" y="4" width="320" height="7" fill="#e8f6f3"/>
    <g fill="#c8ccd4">
      <rect x="8" y="22" width="60" height="3"/><rect x="8" y="40" width="40" height="3"/><rect x="8" y="72" width="30" height="3"/>
      <rect x="8" y="104" width="24" height="3"/><rect x="8" y="136" width="50" height="3"/><rect x="8" y="150" width="44" height="3"/>
      <rect x="150" y="40" width="80" height="3"/><rect x="150" y="46" width="110" height="3"/><rect x="150" y="72" width="80" height="3"/>
      <rect x="150" y="78" width="110" height="3"/><rect x="150" y="104" width="60" height="3"/><rect x="150" y="110" width="40" height="3"/>
      <rect x="150" y="136" width="70" height="3"/><rect x="150" y="150" width="90" height="3"/>
    </g>
    <g fill="#dfe2e8"><rect x="290" y="38" width="22" height="7"/><rect x="290" y="70" width="22" height="7"/><rect x="290" y="102" width="22" height="7"/><rect x="290" y="134" width="22" height="7"/><rect x="290" y="148" width="22" height="7"/></g>
    <rect x="0" y="170" width="320" height="7" fill="#e8f6f3"/><rect x="0" y="184" width="320" height="7" fill="#f2f3f5"/>
  </svg>

  <h3 style="left:88px">Summarized And Linked to<br>Key Insights</h3>
  <h3 style="left:440px">Risk-Adjustment</h3>
  <h3 style="left:791px">Quality Analysis</h3>
  <p style="left:88px;top:366px">Insights are presented in a concise summary with direct links to supporting evidence. HCC, HEDIS and MIPS opportunities are abstracted and cross-linked directly to the original text in the underlying record for quick and easy reference.</p>
  <p style="left:440px;top:366px">HCC opportunities for new capture and recapture are identified and extracted using logic algorithms.</p>
  <p style="left:791px;top:333px">HEDIS and MIPS quality measure gaps closed using HQAB certified technology to generate ORDAII.</p>
</section>

<section class="delivered">
  <h2 class="sec-title" style="top:56px">Delivered Directly into Your EHR for Native Viewing</h2>
  <p class="sec-sub" style="top:114px;font-size:15.5px;line-height:24px">The final package is delivered as a single longitudinal record into each patient’s chart within your EHR, viewable natively<br>The Clinivue Lumora is compatible with any Meaningful Use certified EHR.</p>
  <div class="ehr-row">
    <div class="ehr">Allvantis</div><div class="ehr">northchart</div><div class="ehr">Corvant</div><div class="ehr">Ember</div>
    <div class="ehr">Halden Care</div><div class="ehr">Greystone</div><div class="ehr">MERIDEX</div><div class="ehr">Vitalis</div>
  </div>
  <div class="tablet-frame">
    <div class="tablet">
      <svg class="screen" viewBox="0 0 405 306">
        <rect width="405" height="306" fill="#fff"/>
        <rect width="405" height="10" fill="#3a3f4a"/><rect y="10" width="405" height="14" fill="#0355a3"/>
        <rect x="40" y="42" width="8" height="8" fill="#0355a3"/><rect x="52" y="44" width="52" height="4" fill="#555"/>
        <rect x="160" y="42" width="70" height="4" fill="#555"/><rect x="300" y="42" width="50" height="4" fill="#555"/>
        <rect x="40" y="70" width="330" height="7" fill="#e4e6ea"/>
        <g fill="#c8ccd4">
          <rect x="40" y="84" width="220" height="3"/><rect x="40" y="96" width="200" height="3"/><rect x="40" y="108" width="230" height="3"/>
          <rect x="40" y="120" width="190" height="3"/><rect x="40" y="132" width="210" height="3"/><rect x="40" y="144" width="180" height="3"/>
          <rect x="40" y="156" width="220" height="3"/><rect x="40" y="168" width="170" height="3"/><rect x="40" y="180" width="200" height="3"/>
          <rect x="40" y="192" width="150" height="3"/><rect x="40" y="204" width="100" height="3"/><rect x="40" y="216" width="120" height="3"/>
          <rect x="40" y="228" width="200" height="3"/>
        </g>
        <g fill="#33b8a4"><rect x="300" y="84" width="16" height="3"/><rect x="300" y="108" width="16" height="3"/><rect x="300" y="132" width="16" height="3"/><rect x="300" y="156" width="16" height="3"/><rect x="300" y="180" width="16" height="3"/><rect x="300" y="216" width="16" height="3"/></g>
        <rect y="260" width="405" height="46" fill="#c9ccd2"/><rect x="200" y="260" width="205" height="46" fill="#e4e6ea"/>
      </svg>
      <svg class="abs" style="left:472px;top:162px" width="24" height="24"><circle cx="12" cy="12" r="11" fill="#dfe1e5"/></svg>
    </div>
  </div>
</section>

<section class="features">
  <div class="feat" style="left:203px">
    <svg width="66" height="66" viewBox="0 0 66 66"><circle cx="33" cy="33" r="30" fill="none" stroke="#00a990" stroke-width="3"/><circle cx="33" cy="33" r="18" fill="none" stroke="#6b449b" stroke-width="3"/><path d="M33 26 L40 33 L33 40 L26 33 Z" fill="#fff"/></svg>
    <h3>Click Access</h3><p>Click access to each inference and insight in the underlying record</p>
  </div>
  <div class="feat" style="left:468px">
    <svg width="66" height="66" viewBox="0 0 66 66"><path d="M40 5 A29 29 0 1 1 12 14" fill="none" stroke="#00a990" stroke-width="3"/><path d="M12 8 L22 20 M22 14 V20 H16" fill="none" stroke="#6b449b" stroke-width="3"/><path d="M33 26 L40 33 L33 40 L26 33 Z" fill="#fff"/></svg>
    <h3>Searchable</h3><p>All data in the Lumora CCDA is searchable, including previously unstructured data</p>
  </div>
  <div class="feat" style="left:732px">
    <svg width="80" height="66" viewBox="0 0 80 66"><circle cx="30" cy="33" r="28" fill="none" stroke="#6b449b" stroke-width="3"/><circle cx="50" cy="33" r="28" fill="none" stroke="#00a990" stroke-width="3"/><path d="M40 26 L47 33 L40 40 L33 33 Z" fill="#fff"/></svg>
    <h3>Seamless Integration</h3><p>Designed for seamless integration into your current tools and workflow</p>
  </div>
  <div class="feat" style="left:996px">
    <svg width="66" height="66" viewBox="0 0 66 66" stroke-width="3" stroke-linecap="round"><g stroke="#6b449b"><path d="M33 4 V14 M33 52 V62 M4 33 H14 M52 33 H62"/></g><g stroke="#00a990"><path d="M13 13 L19 19 M47 47 L53 53 M53 13 L47 19 M13 53 L19 47"/></g><path d="M33 26 L40 33 L33 40 L26 33 Z" fill="#fff"/></svg>
    <h3>Empower Physicians</h3><p>Provide physicians with a complete summarized medical history linked to supporting documentation ahead of every encounter</p>
  </div>
</section>

<section class="blog">
  <h2 class="sec-title" style="top:52px">Latest Blog Posts</h2>
  <article class="post" style="left:88px">
    <div class="post-img" role="img" aria-label="Photo of a pen over printed financial charts"></div>
    <div class="post-cap">There are many variations of dummy printing ...</div>
    <a class="btn btn-teal">Read More</a>
  </article>
  <article class="post" style="left:440px">
    <div class="post-img dark" role="img" aria-label="Photo of a businessman in a suit against a city skyline"></div>
    <div class="post-cap">There are many variations of dummy printing ...</div>
    <a class="btn btn-purple">Read More</a>
  </article>
  <article class="post" style="left:791px">
    <div class="post-img" role="img" aria-label="Photo of analytics charts on a laptop screen"></div>
    <div class="post-cap">There are many variations of dummy printing ...</div>
    <a class="btn btn-teal">Read More</a>
  </article>
</section>

<footer class="site-footer">
  <p style="top:40px">The Clinivue Lumora is a game-changing tool designed to accelerate success in value-based contracts by maximizing outcomes, scores and revenue while significantly decreasing inefficiencies and administrative burden.</p>
  <p style="top:98px">Clinivue platform has been shaped by our partnerships with the leaders in value-based care to address their most complex challenges. We are experts in interoperability technology who are passionate about empowering healthcare organizations to achieve market-leading results.</p>
  <p class="legal" style="top:212px">© Copyright CLINIVUE 2020 | All Rights Reserved.</p>
  <div class="foot-mark"></div>
</footer>

</body>
</html>
```